Corporate-Design für Patentanwaltskanzlei
Zielgruppe
Patentanwaltskanzlei mit drei Partnern: Brandl, Hofmann und Lorenz. Wenn Namenshinweis im Logo ist, sollte Brandl (S) an erster Stelle sein. Gerne aber auch Fantasiename.
Kanzlei zielt auf deutsche Mittelständler & Industrie in neuen Technologien, z.B. Medizintechnik, Umweltechnik, Lebenmitteltechnoloie, Sensortechnik weniger auf klassischen Automobilbau
; unser Background ist E-Technik/Maschbau/Physik.
Wir haben Industriehintergrund z.T. in leitenden Postionen, eine Eigenschaft, die uns von anderen Kanzleien abhebt.
Wir sehen unseren Service als Dreieck aus Rechts-, Techologie- und Businessberatung, diese stehen in gegenseitigem Verhältnis zueinander.
Aufgabenstellung
Eher modern, und clean. Gerne auch Fanasienamen und Kombination aus Logo und Namen oder integriert darin, der auf das obige und unsere Dienstleistung hinweist. fantasiename wäre unabhängig von Namen wenn diese sich später änderns sollten. Ein reines Logo wäre vermutlich zuwenig, da Mandanten üblicherwesie den Namen verwenden. Üblicherweise sagt kein Mensch ausformulierte Dreifachnahmen, daher kürzer ist besser, z.B. Pimbo oder RNW.

```html
<!DOCTYPE html>
<html lang="de">
<head>
<meta charset="utf-8">
<title>Corporate Design – Patentanwaltkanzlei Brandl · Hofmann · Lorenz</title>
<link href="https://fonts.googleapis.com/css2?family=Barlow+Condensed:ital,wght@1,700&family=Cinzel:wght@700&family=Open+Sans:wght@400&family=Libre+Bodoni:ital,wght@1,500&family=Arimo:ital,wght@1,700&display=swap" rel="stylesheet">
<style>
  :root{
    --ink:#000;
    --brand:#333333;
    --rule:#9a9a9a;
    --paper:#ffffff;
    --faint:#f1f1f1;
    --bar:#9b9b9b;
  }
  *{box-sizing:border-box;margin:0;padding:0}
  html,body{width:1200px;height:928px;overflow:hidden;background:var(--paper)}
  .canvas{position:relative;width:1200px;height:928px;color:var(--ink);font-family:"Open Sans",Arial,sans-serif}
  .abs{position:absolute}

  .heading{position:absolute;font-family:"Barlow Condensed","Arial Narrow",sans-serif;font-weight:700;font-style:italic;line-height:1;white-space:nowrap}
  .heading--main{left:272px;top:14px;font-size:80px}
  .heading--section{font-size:46px}

  /* logo replacement */
  .mark{position:absolute;border-radius:50%;background:var(--brand)}
  .mark--light{background:var(--paper)}
  .wordmark{position:absolute;font-family:"Cinzel",Georgia,serif;font-weight:700;color:var(--brand);text-align:center;white-space:nowrap;line-height:1}
  .wordmark--light{color:var(--paper)}
  .wordmark__rule{position:absolute;height:2px;background:var(--brand)}
  .wordmark__rule--light{background:var(--paper)}

  /* letterhead */
  .letter{left:2px;top:223px;width:496px;height:694px;border:1.5px solid var(--ink);background:var(--paper);overflow:hidden}
  .letter__bar{position:absolute;left:0;top:0;width:13px;height:100%;background:var(--bar)}
  .letter__watermark{position:absolute;left:118px;top:240px;width:250px;height:250px;border-radius:50%;background:var(--faint)}
  .letter__line{position:absolute;height:2px;background:var(--rule)}
  .letter__text{position:absolute;font-size:8.5px;line-height:10.6px;white-space:pre}
  .letter__small{position:absolute;font-size:5.8px;line-height:7.2px;white-space:pre}
  .letter__body{position:absolute;font-size:9.5px;line-height:12.5px;white-space:pre}

  /* business cards */
  .card{position:absolute;width:310px;height:200px;border:1.5px solid var(--ink);background:var(--paper);overflow:hidden}
  .card--dark{background:var(--brand);border-color:var(--brand)}
  .card__band{position:absolute;left:0;top:0;width:100%;height:45px;background:var(--brand)}
  .card__tagline{position:absolute;left:68px;top:16px;font-family:"Libre Bodoni",Georgia,serif;font-style:italic;font-weight:500;font-size:10.5px;color:var(--paper);white-space:nowrap}
  .card__name{position:absolute;left:0;width:116px;top:91px;text-align:center;font-family:"Libre Bodoni",Georgia,serif;font-style:italic;font-weight:500;font-size:17.5px;line-height:21px;color:#555}
  .card__namerule{position:absolute;left:9px;top:134px;width:98px;height:1.5px;background:var(--ink)}
  .card__role{position:absolute;left:0;width:116px;top:139px;text-align:center;font-family:"Arimo",Arial,sans-serif;font-weight:700;font-size:9px}
  .card__divider{position:absolute;left:115px;top:92px;width:1.5px;height:97px;background:var(--ink)}
  .card__contact{position:absolute;left:125px;top:103px;font-family:"Arimo",Arial,sans-serif;font-style:italic;font-weight:700;font-size:10px;line-height:13.5px;border-collapse:collapse}
  .card__contact td{padding:0;white-space:nowrap}
  .card__contact td:first-child{width:51px}
  .card__contact .gap td{height:12px}
</style>
</head>
<body>
<div class="canvas">

  <h1 class="heading heading--main">Corporate Design</h1>
  <h2 class="heading heading--section" style="left:94px;top:160px">Briefpapierdesign</h2>
  <h2 class="heading heading--section" style="left:910px;top:210px">Logodesign</h2>
  <h2 class="heading heading--section" style="left:744px;top:421px">Visitenkartendesign</h2>

  <!-- letterhead -->
  <section class="abs letter" aria-label="Briefpapier">
    <div class="letter__bar"></div>
    <div class="letter__watermark"></div>

    <div class="mark" style="left:342px;top:12px;width:58px;height:58px"></div>
    <div class="letter__line" style="left:25px;top:62px;width:298px"></div>
    <div class="letter__line" style="left:414px;top:62px;width:72px"></div>
    <div class="wordmark" style="left:280px;top:77px;width:200px;font-size:10.5px">PATENTANWALTKANZLEI</div>
    <div class="wordmark__rule" style="left:300px;top:90px;width:158px;height:1px"></div>
    <div class="wordmark" style="left:280px;top:94px;width:200px;font-size:8.5px">BRANDL · HOFMANN · LORENZ</div>

    <div class="letter__small" style="left:56px;top:110px">BHL Kanzlei------------------------------------------------</div>
    <div class="letter__text" style="left:60px;top:125px">------------------------------------
-----------------------------
------------------------------------</div>

    <div class="letter__text" style="left:331px;top:125px">BHL Kanzlei
Adresse -----------------
Stadt ---------------------

Tel.:    -------------------
E-Mail:    ----------------
Website:   ---------------
Datum: 10.07.2021
Kunden Nr.: ------------</div>

    <div class="letter__body" style="left:58px;top:313px">Sehr geehrte Damen und Herren,</div>
    <div class="letter__body" style="left:58px;top:337px">--------------------------------------------------------------------------
--------------------------------------------------------------------------
--------------------------------------------------------------------------
-------------------------

--------------------------------------------------------------------
----------------------------------------------------------------------
--------------------------------------------------------------------------</div>
    <div class="letter__body" style="left:58px;top:443px">Herzliche Grüße
BHL Kanzlei</div>

    <div class="letter__line" style="left:28px;top:605px;width:443px"></div>
    <div class="letter__small" style="left:25px;top:632px">BHL Kanzlei
Inh. -------------------------
Adressdaten-------------
--------------------------------</div>
    <div class="letter__small" style="left:141px;top:632px">Tel.:  ---------------------------
E-Mail:  -------------------
Website: --------------------</div>
    <div class="letter__small" style="left:272px;top:632px">Bank--------------------
BLZ:  ------------------
KTO: -------------------
KTO Inh.:  -----------</div>
    <div class="letter__small" style="left:368px;top:632px">Steuer-Nr.: ---------------
Finanzamt ---------------</div>
  </section>

  <!-- primary logo -->
  <section aria-label="Logo">
    <div class="mark" style="left:738px;top:180px;width:120px;height:120px"></div>
    <div class="wordmark" style="left:625px;top:314px;width:340px;font-size:21px">PATENTANWALTKANZLEI</div>
    <div class="wordmark__rule" style="left:655px;top:340px;width:280px"></div>
    <div class="wordmark" style="left:625px;top:352px;width:340px;font-size:17px">BRANDL · HOFMANN · LORENZ</div>
  </section>

  <!-- business cards -->
  <section class="card" style="left:570px;top:486px" aria-label="Visitenkarte Vorderseite hell">
    <div class="mark" style="left:107px;top:20px;width:96px;height:96px"></div>
    <div class="wordmark" style="left:0;top:130px;width:307px;font-size:15.5px">PATENTANWALTKANZLEI</div>
    <div class="wordmark__rule" style="left:48px;top:149px;width:212px;height:1.5px"></div>
    <div class="wordmark" style="left:0;top:158px;width:307px;font-size:12.5px">BRANDL · HOFMANN · LORENZ</div>
  </section>

  <section class="card" style="left:890px;top:486px" aria-label="Visitenkarte Rückseite">
    <div class="card__band"></div>
    <div class="mark mark--light" style="left:17px;top:6px;width:32px;height:32px"></div>
    <div class="card__tagline">Rechts-, Techologie- und Businessberatung</div>
    <div class="card__name">Vorname<br>Brandl</div>
    <div class="card__namerule"></div>
    <div class="card__role">Rechtsanwalt</div>
    <div class="card__divider"></div>
    <table class="card__contact">
      <tr><td>Tel.</td><td>+49 12345678</td></tr>
      <tr><td>Fax</td><td>+49 12345678</td></tr>
      <tr><td>Mobil</td><td>+49 12345678</td></tr>
      <tr class="gap"><td></td><td></td></tr>
      <tr><td>E-Mail</td><td>kontakt@bhl-kanzlei.de</td></tr>
      <tr><td>Web</td><td>www.bhl-kanzlei.de</td></tr>
    </table>
  </section>

  <section class="card card--dark" style="left:570px;top:727px" aria-label="Visitenkarte Vorderseite dunkel">
    <div class="mark mark--light" style="left:114px;top:20px;width:82px;height:82px"></div>
    <div class="wordmark wordmark--light" style="left:0;top:123px;width:307px;font-size:15.5px">PATENTANWALTKANZLEI</div>
    <div class="wordmark__rule wordmark__rule--light" style="left:48px;top:142px;width:212px;height:1.5px"></div>
    <div class="wordmark wordmark--light" style="left:0;top:152px;width:307px;font-size:12.5px">BRANDL · HOFMANN · LORENZ</div>
  </section>

  <section class="card" style="left:890px;top:727px" aria-label="Visitenkarte Rückseite">
    <div class="card__band"></div>
    <div class="mark mark--light" style="left:17px;top:6px;width:32px;height:32px"></div>
    <div class="card__tagline">Rechts-, Techologie- und Businessberatung</div>
    <div class="card__name">Vorname<br>Brandl</div>
    <div class="card__namerule"></div>
    <div class="card__role">Rechtsanwalt</div>
    <div class="card__divider"></div>
    <table class="card__contact">
      <tr><td>Tel.</td><td>+49 12345678</td></tr>
      <tr><td>Fax</td><td>+49 12345678</td></tr>
      <tr><td>Mobil</td><td>+49 12345678</td></tr>
      <tr class="gap"><td></td><td></td></tr>
      <tr><td>E-Mail</td><td>kontakt@bhl-kanzlei.de</td></tr>
      <tr><td>Web</td><td>www.bhl-kanzlei.de</td></tr>
    </table>
  </section>

</div>
</body>
</html>
```